Business Card Design - Furniture Retail

Open to both Single or double sided design

We are launching a online ecommerce store that sells Scandinavian/Danish style of furniture in Australia.

We aspire to provide stylish but classic and designers' selection of furniture to the Australia public at affordable price. For the style of the furniture we are selling, please see the following links:

https://www.boxlyshare.com/sh/qrk7vz2mwpl04tn/BBXTpeLr3h52Kd7nWqYzRsGmu?dl=0

The style of the design we are looking for is clean, simple that look Scandinavian/Danish but yet it is timeless classic.

Aspiring Design
http://www.hallwick.com
http://brenlowe.com.au/
http://kolvo.furniture/
http://www.tipo.com/
Updates

Please display the card on normal angle for both front and back instead of funny angle. Please keep it display when displaying the design of the business cards so that we can focus on the designs rather than being confused by the unnecessary stuffs like the hands or background

I think there is already enough curve line on the logo itself so anything extra of the curve on the business card would be really unnecessary. Please avoid using any of the extra curve line on the business card, other than the logo itself. Thanks

Regular card and give them a matt celloglaze to create texture on card that makes it looked luxury and expensive.

Please display design on normal angle! Please only use white colour in the background (not the business card but the referring to the submission) rather than anything fancy so that we can focus on the design.

Target Market(s)

High end market consumers who are financially capable and who has good taste and appreciate good design

aged between 28 - 45 white collars professional/businessmen who live in metropolitan areas

Industry/Entity Type

Business

Font styles to use
Serif
Sans Serif

Requirements
Must have
• Regular card and give them a matt celloglaze to create texture on card that makes it looked luxury and expensive.

Please use the logo from the uploaded files

Company Name: Miles Orveda
Name: Peter Holm
Phone: +614 27 505 316
Website: www.milesorveda.com.au
Email: peter@milesorveda.com.au
Nice to have
• Colour is not limited to black and white
Should not have
• The concept photos of the furniture should NOT be used in the FRONT page of the business card.

```html
<!DOCTYPE html>
<html lang="en">
<head>
<meta charset="utf-8">
<title>Miles Orveda – Business Card</title>
<link rel="stylesheet" href="https://fonts.googleapis.com/css2?family=Josefin+Sans:wght@400;600&display=swap">
<style>
  :root {
    --page: #ffffff;
    --ink: #111111;
    --paper: #ffffff;
    --band: #050505;
    --mist: #c9d6dc;
    --photo-top: #dfe4e8;
    --photo-mid: #b9c6cf;
    --photo-low: #3e5168;
    --text-dark: #1c1c1c;
    --text-light: #ffffff;
  }
  * { margin: 0; padding: 0; box-sizing: border-box; }
  html, body {
    width: 1127px;
    height: 1200px;
    overflow: hidden;
    background: var(--page);
    font-family: "Josefin Sans", "Helvetica Neue", Arial, sans-serif;
    color: var(--text-dark);
  }
  .sheet {
    position: relative;
    width: 1127px;
    height: 1200px;
  }
  .card {
    position: absolute;
    left: 124px;
    width: 880px;
    height: 510px;
    background: var(--paper);
    overflow: hidden;
    box-shadow: 0 2px 10px rgba(0,0,0,0.12), 0 0 0 1px rgba(0,0,0,0.06);
  }
  .card--details { top: 60px; }
  .card--brand { top: 630px; }

  /* details side */
  .card__photo {
    position: absolute;
    left: 0; top: 0;
    width: 100%;
    height: 196px;
    background: linear-gradient(180deg, var(--photo-top) 0%, var(--photo-mid) 55%, var(--photo-low) 100%);
  }
  .card__band {
    position: absolute;
    left: 0; top: 196px;
    width: 100%;
    height: 112px;
    background: var(--band);
  }
  .wordmark {
    font-family: "Josefin Sans", "Helvetica Neue", Arial, sans-serif;
    font-weight: 400;
    color: var(--text-light);
    text-transform: uppercase;
    letter-spacing: 0.04em;
    white-space: nowrap;
  }
  .card__band .wordmark {
    position: absolute;
    left: 250px;
    top: 44px;
    font-size: 46px;
    line-height: 1;
  }
  .card__accent {
    position: absolute;
    left: 430px;
    bottom: 0;
    right: 0;
    height: 62px;
    background: var(--mist);
  }
  .contact {
    position: absolute;
    font-size: 27px;
    line-height: 1;
    color: var(--text-dark);
    white-space: nowrap;
  }
  .contact--web { right: 36px; top: 348px; }
  .contact--mail { right: 36px; top: 412px; }
  .contact--name { left: 54px; top: 418px; }
  .contact--phone { left: 54px; top: 466px; }

  /* brand side */
  .card--brand { background: var(--band); }
  .card__strip {
    position: absolute;
    left: 0; width: 100%;
    background: var(--paper);
  }
  .card__strip--top { top: 0; height: 40px; }
  .card__strip--bottom { bottom: 0; height: 72px; }
  .card--brand .wordmark {
    position: absolute;
    left: 0; right: 0;
    top: 208px;
    text-align: center;
    font-size: 50px;
    line-height: 1;
  }
</style>
</head>
<body>
  <main class="sheet">
    <section class="card card--details" aria-label="Business card, details side">
      <div class="card__photo" role="img" aria-label="Photo of a Scandinavian living room with a navy sofa, cushions, side tables and a shelf"></div>
      <div class="card__band">
        <span class="wordmark">Miles Orveda</span>
      </div>
      <div class="card__accent"></div>
      <p class="contact contact--web">www.milesorveda.com.au</p>
      <p class="contact contact--mail">peter@milesorveda.com.au</p>
      <p class="contact contact--name">Peter Holm</p>
      <p class="contact contact--phone">+614 27 505 316</p>
    </section>

    <section class="card card--brand" aria-label="Business card, brand side">
      <div class="card__strip card__strip--top"></div>
      <span class="wordmark">Miles Orveda</span>
      <div class="card__strip card__strip--bottom"></div>
    </section>
  </main>
</body>
</html>
```